Generic fund comparison

We need a power point template to be used for presentation decks and proposals to clients and prospects. We are an independent Registered Investment Advisor in Pittsburgh Pennsylvania.
Our services include family office, alternative investments, investment management, financial planning and consulting.
We would like to see designs that use the color green and grey as they are part of our logo and brand image. The final design should communicate our guiding principles: 'educate, plan, implement, adapt'

```html
<!DOCTYPE html>
<html lang="en">
<head>
<meta charset="utf-8">
<title>Fund comparison deck template</title>
<link rel="stylesheet" href="https://fonts.googleapis.com/css2?family=Open+Sans:wght@400;600;700;800&display=swap">
<style>
:root{
  --green:#7cc242;
  --green-dark:#5e9f2c;
  --green-pale:#dff0cf;
  --grey:#5a5f63;
  --grey-light:#d9dcde;
  --ink:#2b2f33;
  --paper:#ffffff;
  --sheet:#eef0ef;
  --pink:#f6c9d1;
}
*{box-sizing:border-box;margin:0;padding:0}
html,body{width:849px;height:1200px;overflow:hidden;background:var(--sheet);font-family:"Open Sans",Arial,sans-serif;color:var(--ink)}
.sheet{position:relative;width:849px;height:1200px}
.slide{position:absolute;width:388px;height:224px;background:var(--paper);box-shadow:0 1px 4px rgba(0,0,0,.18);overflow:hidden}
.col-a{left:22px}.col-b{left:438px}
.row-1{top:10px}.row-2{top:247px}.row-3{top:484px}.row-4{top:721px}.row-5{top:958px}

/* cover */
.cover-band{position:absolute;left:0;top:0;width:100%;height:128px;background:var(--green);display:flex;flex-direction:column;align-items:center;justify-content:center;text-align:center;color:#fff}
.cover-band.photo{background:linear-gradient(135deg,#8fd052 0%,#6fb83a 45%,#a6d97b 70%,#79c044 100%)}
.cover-title{font-size:14.5px;font-weight:600;letter-spacing:.4px;line-height:1.2;text-transform:uppercase;width:320px;margin-top:8px}
.cover-date{font-size:6px;margin-top:6px;opacity:.9}
.cover-brand{position:absolute;left:0;right:0;top:150px;text-align:center}
.brand-name{font-size:8px;font-weight:700;letter-spacing:1.5px;color:var(--grey)}
.cover-foot{position:absolute;left:0;bottom:0;width:100%;height:38px;background:var(--green)}

/* content slide */
.slide-title{position:absolute;left:14px;top:12px;font-size:14px;font-weight:700;color:var(--ink);padding-left:8px;border-left:3px solid var(--green);line-height:1.1}
.chart{position:absolute;left:14px;top:40px;width:360px;height:150px}
.foot{position:absolute;left:0;bottom:0;width:100%;height:22px;background:var(--green);color:#fff;font-size:5px;display:flex;align-items:center;justify-content:center}

/* tables */
.data{position:absolute;left:70px;top:42px;width:250px;border-collapse:collapse;font-size:5px}
.data th{background:var(--grey);color:#fff;font-weight:600;padding:2px 4px;text-align:center}
.data td{padding:1.6px 4px;border-bottom:1px solid var(--grey-light);text-align:center}
.data td:first-child{text-align:left}
.data.returns td{background:var(--green-pale)}
.data.returns td.neg{background:var(--pink)}

/* disclaimer */
.disclaimer{position:absolute;left:14px;right:14px;top:42px;font-size:5.6px;line-height:1.6;color:var(--grey);text-align:justify}
.disclaimer p+p{margin-top:5px}
</style>
</head>
<body>
<main class="sheet">

  <section class="slide col-a row-1">
    <div class="cover-band">
      <h1 class="cover-title">Independent financial advisory services tailored to your goals</h1>
      <p class="cover-date">ABC, XYZ – April 2024</p>
    </div>
    <div class="cover-brand"><span class="brand-name">VERDANT</span></div>
  </section>

  <section class="slide col-b row-1">
    <div class="cover-band photo" role="img" aria-label="Green tinted photo of city office towers behind the title">
      <h1 class="cover-title">Independent financial advisory services tailored to your goals</h1>
      <p class="cover-date">ABC, XYZ – April 2024</p>
    </div>
    <div class="cover-brand"><span class="brand-name">VERDANT</span></div>
    <div class="cover-foot"></div>
  </section>

  <section class="slide col-a row-2">
    <h2 class="slide-title">ABC, XYZ – Growth of $1.000 vs Benchmark</h2>
    <svg class="chart" viewBox="0 0 360 150">
      <g stroke="#e5e7e8" stroke-width=".6"><path d="M20 20H350M20 45H350M20 70H350M20 95H350M20 120H350"/></g>
      <path d="M20 135H350M20 10V135" stroke="#999" stroke-width=".6"/>
      <polyline fill="none" stroke="#7cc242" stroke-width="1" points="20,130 45,126 70,120 95,118 120,110 145,104 170,100 195,96 220,84 245,76 270,66 295,54 320,44 345,30"/>
      <polyline fill="none" stroke="#3d7fc1" stroke-width="1" points="20,130 45,124 70,122 95,115 120,112 145,102 170,98 195,90 220,86 245,72 270,62 295,58 320,40 345,34"/>
      <polyline fill="none" stroke="#e4a13a" stroke-width="1" points="20,130 45,128 70,118 95,116 120,106 145,106 170,94 195,92 220,80 245,78 270,70 295,50 320,48 345,26"/>
      <polyline fill="none" stroke="#555" stroke-width=".8" points="20,130 45,127 70,124 95,120 120,116 145,110 170,104 195,100 220,94 245,86 270,78 295,70 320,60 345,50"/>
    </svg>
    <div class="foot">Benchmark: 60% equity / 40% bond index</div>
  </section>

  <section class="slide col-b row-2">
    <h2 class="slide-title">ABC, XYZ – Annual Returns vs Benchmark*</h2>
    <table class="data returns">
      <tr><th>Year</th><th>ABC</th><th>XYZ</th><th>Bench</th></tr>
      <tr><td>2013</td><td>12.4%</td><td>10.1%</td><td>11.2%</td></tr>
      <tr><td>2014</td><td>6.3%</td><td>5.8%</td><td>6.0%</td></tr>
      <tr><td>2015</td><td class="neg">-1.2%</td><td class="neg">-0.8%</td><td>0.4%</td></tr>
      <tr><td>2016</td><td>7.9%</td><td>8.4%</td><td>7.1%</td></tr>
      <tr><td>2017</td><td>14.2%</td><td>13.0%</td><td>12.6%</td></tr>
      <tr><td>2018</td><td class="neg">-4.6%</td><td class="neg">-3.9%</td><td class="neg">-3.2%</td></tr>
      <tr><td>2019</td><td>18.1%</td><td>16.7%</td><td>17.3%</td></tr>
      <tr><td>2020</td><td>9.8%</td><td>11.2%</td><td>10.4%</td></tr>
      <tr><td>2021</td><td>13.5%</td><td>12.1%</td><td>12.9%</td></tr>
      <tr><td>2022</td><td class="neg">-9.4%</td><td class="neg">-8.7%</td><td class="neg">-10.1%</td></tr>
      <tr><td>2023</td><td>11.6%</td><td>10.9%</td><td>11.0%</td></tr>
      <tr><td>YTD</td><td>3.2%</td><td>2.8%</td><td>3.0%</td></tr>
    </table>
    <div class="foot">Benchmark: 60% equity / 40% bond index</div>
  </section>

  <section class="slide col-a row-3">
    <h2 class="slide-title">ABC, XYZ – Risk / Return vs Benchmark*</h2>
    <svg class="chart" viewBox="0 0 360 150">
      <g stroke="#e5e7e8" stroke-width=".6" stroke-dasharray="2 2"><path d="M20 30H350M20 60H350M20 90H350M20 120H350"/></g>
      <path d="M20 135H350M20 10V135" stroke="#999" stroke-width=".6"/>
      <circle cx="150" cy="70" r="3" fill="#7cc242"/>
      <circle cx="175" cy="82" r="3" fill="#3d7fc1"/>
      <circle cx="205" cy="58" r="3" fill="#e4a13a"/>
      <circle cx="130" cy="92" r="3" fill="#555"/>
    </svg>
    <div class="foot">Annualised return vs standard deviation</div>
  </section>

  <section class="slide col-b row-3">
    <h2 class="slide-title">ABC, XYZ – analytical data vs Benchmark*</h2>
    <table class="data">
      <tr><th>Measure</th><th>ABC</th><th>Benchmark</th></tr>
      <tr><td>Annualised return</td><td>7.84%</td><td>6.92%</td></tr>
      <tr><td>Standard deviation</td><td>9.12%</td><td>8.40%</td></tr>
      <tr><td>Sharpe ratio</td><td>0.71</td><td>0.64</td></tr>
      <tr><td>Largest monthly gain</td><td>7.20%</td><td>6.85%</td></tr>
      <tr><td>Largest monthly loss</td><td>-8.10%</td><td>-7.60%</td></tr>
      <tr><td>Max drawdown</td><td>-18.4%</td><td>-16.9%</td></tr>
      <tr><td>Positive months</td><td>64%</td><td>62%</td></tr>
      <tr><td>Beta</td><td>1.04</td><td>1.00</td></tr>
      <tr><td>Alpha (annualised)</td><td>0.62%</td><td>–</td></tr>
      <tr><td>Correlation</td><td>0.93</td><td>1.00</td></tr>
      <tr><td>Tracking error</td><td>2.41%</td><td>–</td></tr>
      <tr><td>Information ratio</td><td>0.38</td><td>–</td></tr>
    </table>
    <div class="foot">Benchmark: 60% equity / 40% bond index</div>
  </section>

  <section class="slide col-a row-4">
    <h2 class="slide-title">ABC, XYZ vs Benchmark* – monthly volatility</h2>
    <svg class="chart" viewBox="0 0 360 150">
      <path d="M20 75H350M20 10V140" stroke="#999" stroke-width=".6"/>
      <path stroke="#7cc242" stroke-width="1.6" d="M26 75V60M34 75V88M42 75V52M50 75V70M58 75V95M66 75V58M74 75V66M82 75V104M90 75V62M98 75V48M106 75V84M114 75V72M122 75V56M130 75V90M138 75V64M146 75V40M154 75V80M162 75V110M170 75V68M178 75V54M186 75V86M194 75V60M202 75V76M210 75V50M218 75V92M226 75V62M234 75V70M242 75V98M250 75V58M258 75V66M266 75V45M274 75V84M282 75V62M290 75V116M298 75V56M306 75V72M314 75V60M322 75V88M330 75V52M338 75V80M346 75V64"/>
      <path stroke="#555" stroke-width=".8" d="M29 75V64M37 75V84M45 75V58M53 75V72M61 75V90M69 75V62M77 75V68M85 75V98M93 75V66M101 75V54M109 75V82M117 75V70M125 75V60M133 75V86M141 75V66M149 75V46M157 75V80M165 75V102M173 75V70M181 75V58M189 75V84M197 75V64M205 75V76M213 75V56M221 75V88M229 75V64M237 75V72M245 75V94M253 75V62M261 75V68M269 75V50M277 75V82M285 75V64M293 75V108M301 75V60M309 75V72M317 75V62M325 75V86M333 75V58M341 75V78M349 75V66"/>
    </svg>
    <div class="foot">Monthly returns, last 10 years</div>
  </section>

  <section class="slide col-b row-4">
    <h2 class="slide-title">ABC, XYZ – Return distribution</h2>
    <svg class="chart" viewBox="0 0 360 150">
      <path d="M40 140H330M40 10V140" stroke="#999" stroke-width=".6"/>
      <g fill="#8a8f93" stroke="#fff" stroke-width=".6">
        <rect x="90" y="132" width="20" height="8"/><rect x="110" y="124" width="20" height="16"/>
        <rect x="130" y="100" width="20" height="40"/><rect x="150" y="60" width="20" height="80"/>
        <rect x="170" y="20" width="20" height="120"/><rect x="190" y="40" width="20" height="100"/>
        <rect x="210" y="90" width="20" height="50"/><rect x="230" y="118" width="20" height="22"/>
        <rect x="250" y="134" width="20" height="6"/>
      </g>
    </svg>
    <div class="foot">Frequency of monthly returns</div>
  </section>

  <section class="slide col-a row-5">
    <h2 class="slide-title">Benchmark* – Return distribution</h2>
    <svg class="chart" viewBox="0 0 360 150">
      <path d="M20 140H350M20 10V140" stroke="#999" stroke-width=".6"/>
      <g fill="#8a8f93" stroke="#fff" stroke-width=".6">
        <rect x="60" y="134" width="22" height="6"/><rect x="82" y="136" width="22" height="4"/>
        <rect x="104" y="130" width="22" height="10"/><rect x="126" y="120" width="22" height="20"/>
        <rect x="148" y="86" width="22" height="54"/><rect x="170" y="40" width="22" height="100"/>
        <rect x="192" y="24" width="22" height="116"/><rect x="214" y="50" width="22" height="90"/>
        <rect x="236" y="100" width="22" height="40"/><rect x="258" y="130" width="22" height="10"/>
        <rect x="280" y="136" width="22" height="4"/>
      </g>
    </svg>
    <div class="foot">Frequency of monthly returns</div>
  </section>

  <section class="slide col-b row-5">
    <h2 class="slide-title">Disclaimer</h2>
    <div class="disclaimer">
      <p>This material is provided for information purposes only and does not constitute an offer or solicitation to buy or sell any security. Past performance is not a guarantee of future results. Figures shown are hypothetical and may differ from actual client accounts due to fees, timing of cash flows and individual portfolio restrictions.</p>
      <p>Benchmark data are drawn from sources believed to be reliable, but their accuracy cannot be guaranteed. Indices are unmanaged and cannot be invested in directly. Returns include reinvestment of dividends and interest and are shown before advisory fees unless otherwise noted.</p>
      <p>Investing involves risk, including possible loss of principal. Alternative investments may be illiquid and are suitable only for qualified investors. Please contact your advisor to discuss whether any strategy described here is appropriate for your goals, time horizon and tolerance for risk.</p>
    </div>
  </section>

</main>
</body>
</html>
```